Custom Cakes- Nonprofit Organization Stationery Set

We are looking for a FULL set stationery design for our organization.
We create custom cakes for children in foster care and work with teens and young adults who have intellectual and developmental disabilities.
We spare no expense or amount of time creating fantastic cakes for these kids.... therefore are marketing materials need to reflect the same amount of fine details.

* Business Card Design (Front/Back preferred)
* Letterhead
* Envelope
* Presentation Folder

**** Tagline: Fostering Amazing Memories
would like this to appear on business card and marketing materials

Marlene Pruitt - Founder/Executive Director
www.brightcrumb.org
info@brightcrumb.org
1-855-MY-CRUMBS
1-855-692-7862

Address is optional
PO Box 7264
Cedar Hollow, TN 30187

• Contact Information
• PO Box Address, design that will go well with textured/colored business card paper
• Updated: Business cards (maybe) textured paper, foiled, embossed or colored edges

```html
<!DOCTYPE html>
<html lang="en">
<head>
<meta charset="utf-8">
<title>Bright Crumb Foundation – Letterhead</title>
<link href="https://fonts.googleapis.com/css2?family=Arimo:wght@400;700&family=Pinyon+Script&display=swap" rel="stylesheet">
<style>
  :root {
    --paper: #ffffff;
    --ink: #231f20;
    --accent-pink: #e23a84;
    --soft-pink: #f6c9df;
    --soft-yellow: #fbf0a8;
    --soft-green: #d8f0b4;
    --soft-blue: #cfe7f3;
    --soft-grey: #e4e4e4;
  }
  html, body {
    margin: 0;
    padding: 0;
    overflow: hidden;
    background: var(--paper);
  }
  .letterhead {
    position: relative;
    width: 928px;
    height: 1200px;
    overflow: hidden;
    background: var(--paper);
    font-family: "Arimo", Arial, sans-serif;
    color: var(--ink);
  }
  .contact-list {
    position: absolute;
    left: 46px;
    top: 54px;
    margin: 0;
    padding: 0;
    list-style: none;
    font-size: 9.6px;
    line-height: 16.2px;
  }
  .contact-list li {
    display: flex;
    align-items: center;
    gap: 5px;
  }
  .contact-list svg {
    width: 11px;
    height: 11px;
    flex: none;
  }
  .contact-list .no-icon {
    padding-left: 16px;
  }
  .brand-name {
    position: absolute;
    right: 60px;
    top: 118px;
    margin: 0;
    width: 160px;
    text-align: center;
    font-size: 19px;
    font-weight: 700;
    line-height: 22px;
    color: var(--accent-pink);
  }
  .brand-mark {
    display: block;
    width: 14px;
    height: 14px;
    margin: 0 auto 6px;
    background: var(--accent-pink);
  }
  .cake-decoration {
    position: absolute;
    left: 518px;
    top: 612px;
    width: 410px;
    height: 588px;
    border-radius: 18px 18px 0 0;
    background: linear-gradient(to bottom,
      var(--soft-yellow) 0%,
      var(--soft-pink) 22%,
      var(--soft-green) 46%,
      var(--soft-blue) 62%,
      var(--soft-grey) 100%);
    opacity: 0.45;
  }
  .letter {
    position: relative;
    z-index: 1;
  }
  .salutation {
    position: absolute;
    left: 75px;
    top: 232px;
    margin: 0;
    font-size: 17px;
  }
  .letter-body {
    position: absolute;
    left: 155px;
    top: 270px;
    width: 708px;
    font-size: 17.1px;
    line-height: 20.6px;
  }
  .letter-body p {
    margin: 0 0 20.6px;
  }
  .letter-body p.continued {
    margin-top: -20.6px;
  }
  .closing {
    position: absolute;
    left: 106px;
    top: 844px;
    margin: 0;
    font-size: 17px;
    line-height: 20.6px;
  }
  .signature {
    position: absolute;
    left: 78px;
    top: 906px;
    margin: 0;
    font-family: "Pinyon Script", cursive;
    font-size: 54px;
    line-height: 60px;
    color: var(--ink);
  }
  .signer-title {
    position: absolute;
    left: 106px;
    top: 970px;
    margin: 0;
    font-size: 17px;
  }
</style>
</head>
<body>
<main class="letterhead">
  <header>
    <ul class="contact-list">
      <li>
        <svg viewBox="0 0 12 12" aria-hidden="true"><path d="M6 .5a4 4 0 0 0-4 4c0 3 4 7 4 7s4-4 4-7a4 4 0 0 0-4-4zm0 5.6a1.6 1.6 0 1 1 0-3.2 1.6 1.6 0 0 1 0 3.2z" fill="var(--accent-pink)"/></svg>
        PO Box 7264, Cedar Hollow, TN 30187
      </li>
      <li>
        <svg viewBox="0 0 12 12" aria-hidden="true"><path d="M2.4 1l2 .2 1 2.6-1.3 1a6.5 6.5 0 0 0 3.1 3.1l1-1.3 2.6 1 .2 2c-.6.8-1.6 1.1-2.6.8C5 9.3 2.7 7 1.6 3.6c-.3-1 0-2 .8-2.6z" fill="var(--accent-pink)"/></svg>
        1-855-692-7862
      </li>
      <li>
        <svg viewBox="0 0 12 12" aria-hidden="true"><rect x="0.5" y="2.5" width="11" height="7" fill="var(--accent-pink)"/><path d="M.8 2.8 6 6.6l5.2-3.8" fill="none" stroke="#fff" stroke-width=".8"/></svg>
        info@brightcrumb.org
      </li>
      <li>
        <svg viewBox="0 0 12 12" aria-hidden="true"><g fill="none" stroke="var(--accent-pink)" stroke-width="1"><circle cx="6" cy="6" r="5"/><ellipse cx="6" cy="6" rx="2.2" ry="5"/><path d="M1 6h10M1.8 3.5h8.4M1.8 8.5h8.4"/></g></svg>
        www.brightcrumb.org
      </li>
      <li class="no-icon">1-855-MY-CRUMBS</li>
    </ul>
    <p class="brand-name"><span class="brand-mark"></span>Bright Crumb Foundation</p>
  </header>

  <div class="cake-decoration" role="img" aria-label="Faint illustration of stacked gift-box cake on a stand"></div>

  <article class="letter">
    <p class="salutation">Dear Sir / Madam,</p>
    <div class="letter-body">
      <p>Lorem ipsum dolor sit amet, consectetur adipisicing elit, sed do eiusmod tempor incididunt ut labore et dolore magna aliqua. Ut enim ad minim veniam, quis nostrud exercitation ullamco laboris nisi ut aliquip ex ea commodo consequa.Lorem ipsum dolor sit amet, consectetur adipisicing elit, sed do eiusmod tempor incididunt ut labore et dolore magna aliqua. Ut enim ad minim veniam, quis.</p>
      <p>Lorem ipsum dolor sit amet, consectetur adipisicing elit, sed do eiusmod tempor incididunt ut labore et dolore magna aliqua. Ut enim ad minim veniam, quis nostrud exercitation ullamco laboris nisi ut aliquip ex ea commodo consequa.Lorem ipsum dolor sit amet, consectetur adipisicing elit, sed do eiusmod tempor incididunt ut labore et dolore magna aliqua. Ut enim ad minim veniam, quis.</p>
      <p>Lorem ipsum dolor sit amet, consectetur adipisicing elit, sed do eiusmod tempor incididunt ut labore et dolore magna aliqua. Ut enim ad minim veniam, quis nostrud exercitation ullamco laboris nisi ut aliquip ex ea commodo consequa.Lorem ipsum dolor sit amet, consectetur adipisicing elit, sed do eiusmod tempor incididunt ut labore et dolore magna aliqua. Ut enim ad minim veniam, quis.</p>
      <p>Lorem ipsum dolor sit amet, consectetur adipisicing elit, sed do eiusmod tempor incididunt ut labore et dolore magna aliqua. Ut enim ad minim veniam, quis nostrud exercitation ullamco laboris nisi ut aliquip ex ea commodo consequa.Lorem ipsum dolor sit amet, consectetur adipisicing elit, sed do eiusmod tempor incididunt ut labore et dolore magna aliqua. Ut enim ad minim veniam, quis.</p>
      <p class="continued">Lorem ipsum dolor sit amet, consectetur adipisicing elit, sed do eiusmod tempor incididunt ut labore et dolore magna aliqua. Ut enim ad minim veniam,</p>
    </div>
    <p class="closing">Best regards,<br>Yours Truly,</p>
    <p class="signature">Your Name</p>
    <p class="signer-title">Company Director</p>
  </article>
</main>
</body>
</html>
```